Business Card Design

Looking for business card designs for a new business. there will be two cards of the same design (both lots of information below in contact info). We would like the logo diagonally across the card with the information split above and below the logo similar to sketch. happy to look at similar alternatives
Please use same colours as in logo design

Industry/Entity Type

Business

Contact Information for Business Card

Colin Marwood
mob - 0498 172 943
ph - 02 6812 4300
fax - 02 6812 4900
email - col@ridgelinetrusses.com.au
14 Larchmont Road, Westdale NSW 2340

Gavin Holloway
mob - 0421 830 576
ph - 02 6812 4300
fax - 02 6812 4900
email - gavin@ridgelinetrusses.com.au

```html
<!DOCTYPE html>
<html lang="en">
<head>
<meta charset="utf-8">
<title>Ridgeline Frames &amp; Trusses – Business Card</title>
<link rel="stylesheet" href="https://fonts.googleapis.com/css2?family=Open+Sans:wght@400;700&display=swap">
<style>
  :root {
    --backdrop: #3e3e3e;
    --card-white: #ffffff;
    --teal: #0e7f7e;
    --ink: #111111;
    --on-teal: #ffffff;
    --divider: rgba(255,255,255,0.75);
  }
  html, body {
    margin: 0;
    padding: 0;
    width: 1200px;
    height: 999px;
    overflow: hidden;
    background: var(--backdrop);
    font-family: "Open Sans", Arial, sans-serif;
  }
  .card {
    position: absolute;
    left: 75px;
    top: 199px;
    width: 1050px;
    height: 600px;
    background: var(--card-white);
    overflow: hidden;
  }
  .card-shapes {
    position: absolute;
    inset: 0;
  }
  .brand {
    position: absolute;
    left: 265px;
    top: 78px;
    width: 520px;
    display: flex;
    align-items: center;
    gap: 18px;
  }
  .brand-mark {
    width: 92px;
    height: 92px;
    background: var(--teal);
    flex: none;
  }
  .brand-name {
    font-weight: 700;
    font-size: 46px;
    line-height: 1.05;
    color: var(--ink);
    letter-spacing: -0.5px;
  }
  .person {
    position: absolute;
    left: 0;
    width: 1050px;
    text-align: center;
    color: var(--ink);
  }
  .person-name {
    top: 274px;
    font-size: 40px;
    font-weight: 700;
  }
  .person-mobile {
    top: 327px;
    left: 430px;
    width: auto;
    font-size: 27px;
    letter-spacing: 0.5px;
  }
  .address {
    position: absolute;
    left: 52px;
    top: 446px;
    margin: 0;
    font-style: normal;
    font-size: 29px;
    line-height: 41.5px;
    color: var(--on-teal);
  }
  .contact-list {
    position: absolute;
    left: 510px;
    top: 444px;
    margin: 0;
    padding: 0;
    list-style: none;
    color: var(--on-teal);
    font-size: 29px;
  }
  .contact-list li {
    display: flex;
    align-items: center;
    height: 42px;
  }
  .contact-icon {
    width: 30px;
    height: 30px;
    flex: none;
  }
  .contact-sep {
    width: 2px;
    height: 30px;
    background: var(--on-teal);
    margin: 0 16px 0 17px;
  }
</style>
</head>
<body>
  <main class="card">
    <svg class="card-shapes" width="1050" height="600" viewBox="0 0 1050 600" aria-hidden="true">
      <path d="M0,354 C300,396 720,392 1050,356 L1050,600 L0,600 Z" fill="#0e7f7e"/>
      <path d="M420,385 C650,386 900,362 1050,326 L1050,348 C900,376 650,393 420,385 Z" fill="#111111"/>
      <line x1="420" y1="412" x2="420" y2="570" stroke="rgba(255,255,255,0.75)" stroke-width="2"/>
    </svg>

    <div class="brand">
      <span class="brand-mark"></span>
      <span class="brand-name">Ridgeline<br>Frames &amp; Trusses</span>
    </div>

    <div class="person person-name">Colin Marwood</div>
    <div class="person person-mobile">0498 172 943</div>

    <address class="address">
      14 Larchmont Road,<br>
      Westdale NSW 2340<br>
      Gavin
    </address>

    <ul class="contact-list">
      <li>
        <svg class="contact-icon" viewBox="0 0 30 30" aria-label="Phone">
          <rect x="0" y="0" width="30" height="30" rx="5" fill="#fff"/>
          <path d="M10,6 L13,6 L14,11 L12,12.5 C13,16 14.5,18 17.5,19 L19,17 L24,18 L24,21 C24,23 22,24 20,24 C13,23 7,17 6,10 C6,8 8,6 10,6 Z" fill="#0e7f7e"/>
        </svg>
        <span class="contact-sep"></span>02 6812 4300
      </li>
      <li>
        <svg class="contact-icon" viewBox="0 0 30 30" aria-label="Fax">
          <rect x="8" y="1" width="14" height="11" fill="#fff"/>
          <rect x="1" y="13" width="28" height="16" rx="3" fill="#fff"/>
          <rect x="7" y="19" width="16" height="3" fill="#0e7f7e"/>
        </svg>
        <span class="contact-sep"></span>02 6812 4900
      </li>
      <li>
        <svg class="contact-icon" viewBox="0 0 30 30" aria-label="Email">
          <path d="M1,12 L15,3 L29,12 L29,27 L1,27 Z" fill="#fff"/>
          <path d="M1,12 L15,21 L29,12" fill="none" stroke="#0e7f7e" stroke-width="2"/>
        </svg>
        <span class="contact-sep"></span>col@ridgelinetrusses.com.au
      </li>
    </ul>
  </main>
</body>
</html>
```